Retail Appliance Store Chain needs NEW business Card

Name of my company is Brandon's Appliances brandonsappliances.com is our website. . We are a 2 location brick and mortar, and online store selling premium, luxury, and normal household appliances, such as ovens, stoves, cooktops, dishwashers, refrigerators, washers and dryers, grills, air conditioners etc. The focus is on large kitchen appliances and laundry appliances.
Please visit http://brandonsappliances.com to get a feel for the business and branding.
I have attached the Brandon's Appliances logo (i do not have eps or psd or ai). And I have also attached our current business cards that we use. We have two versions. A double sided version for managers, and a one side version for regular employees.
Please submit BOTH one sided and two sided designs if possible.
Please keep consistent with the Brandon's Appliances logo, colors, etc.
I would prefer no rounded corners on the business card designs for printing costs.
Information on the cards (in no particular order):
Name - Employee Name
Business name - Brandon's Appliances
website - brandonsappliances.com
Email - Employee Email
2 Phone Numbers - store 1 address, store 2 address
2 Addresses - store 1 address, store 2 address

*do NOT need Fax #

Industry/Entity Type

Home Appliance

Contact Information for Business Card

Logo - Brandons Appliances Logo
Name - Employee Name
Email - Employee Email

Please no rounded corners. Standard US Business Card Size please.

Font styles to use
Serif
Sans Serif

Requirements
Must have
• colors and design that somewhat match the feel of current logo and website
Should not have
• No rounded corners.
No non-traditional business card size. US Standard Business Card Size only

```html
<!DOCTYPE html>
<html lang="en">
<head>
<meta charset="utf-8">
<title>Brandon's Appliances – Business Card</title>
<link rel="stylesheet" href="https://fonts.googleapis.com/css2?family=Roboto:wght@400;700&display=swap">
<style>
  :root {
    --brand-blue: #05417f;
    --card-white: #f8f7fc;
    --backdrop: #9b9b9b;
    --ink-light: #ffffff;
  }
  * { margin: 0; padding: 0; box-sizing: border-box; }
  html, body {
    width: 1200px;
    height: 802px;
    overflow: hidden;
    background: var(--backdrop);
    font-family: "Roboto", Arial, sans-serif;
  }
  .business-card {
    position: absolute;
    left: 100px;
    top: 101px;
    width: 1000px;
    height: 599px;
    background: var(--card-white);
    overflow: hidden;
  }
  .wave-band {
    position: absolute;
    inset: 0;
    width: 100%;
    height: 100%;
  }
  .brand-name {
    position: absolute;
    left: 62px;
    top: 118px;
    color: var(--brand-blue);
    font-weight: 700;
    font-size: 56px;
    line-height: 60px;
  }
  .contact-details {
    position: absolute;
    right: 55px;
    top: 0;
    color: var(--ink-light);
    text-align: right;
  }
  .contact-details p { position: absolute; right: 0; white-space: nowrap; }
  .employee-name { top: 254px; font-size: 37px; font-weight: 700; }
  .employee-email { top: 298px; font-size: 29px; }
  .store-street { top: 358px; font-size: 29px; }
  .store-city { top: 395px; font-size: 29px; }
  .store-phone { top: 462px; font-size: 29px; }
  .store-web { top: 499px; font-size: 29px; }
  .line-icon {
    width: 32px;
    height: 32px;
    vertical-align: -5px;
    margin-left: 8px;
  }
</style>
</head>
<body>
  <section class="business-card">
    <svg class="wave-band" viewBox="0 0 1000 599" aria-hidden="true">
      <path d="M0,346 C30,420 110,430 210,402 C420,340 700,170 968,0 L1000,0 L1000,599 L0,599 Z" fill="var(--brand-blue)"/>
      <path d="M4,366 C40,432 115,440 215,412 C425,350 705,180 985,2" fill="none" stroke="var(--card-white)" stroke-width="5"/>
    </svg>

    <h1 class="brand-name">Brandon's<br>Appliances</h1>

    <div class="contact-details">
      <p class="employee-name">DANIEL REYES</p>
      <p class="employee-email">daniel@brandonsappliances.com</p>
      <p class="store-street">145 Harbor View Rd</p>
      <p class="store-city">Millbrook, CT 06999</p>
      <p class="store-phone">(555) 014-2093<svg class="line-icon" viewBox="0 0 32 32" aria-hidden="true"><rect x="2" y="2" width="28" height="28" rx="4" fill="none" stroke="#fff" stroke-width="2.5"/><path d="M10 8 l4 0 l1.5 5 l-2.5 2 c1.2 2.5 2.5 3.8 5 5 l2 -2.5 l5 1.5 l0 4 c-9 1 -16 -6 -15 -15z" fill="#fff"/></svg></p>
      <p class="store-web">www.brandonsappliances.com<svg class="line-icon" viewBox="0 0 32 32" aria-hidden="true"><g fill="none" stroke="#fff" stroke-width="2.2"><circle cx="16" cy="16" r="13"/><ellipse cx="16" cy="16" rx="6" ry="13"/><path d="M3 16h26M5 9h22M5 23h22"/></g></svg></p>
    </div>
  </section>
</body>
</html>
```